Flyer for The Quiet Bloom Gathering

I am launching my new offering in my business at an event next Sunday where I have a booth and need a flyer advertising the offering, so the flyer needs to stand out for other practitioners that will also be there on the day offering there services.
This flyer is also what I will use for marketing on social media as well as on the day of the event. See the link below to the offering
http://sarahlindqvist.com.au/quiet-bloom-gathering/

Target Market(s)

Women with body image issues - age range 25 - 65
Women with issues around food such as binge eating, emotional eating, eating disorders.

Industry/Entity Type

Health And Wellness

Font styles to use
Serif
Sans Serif
Script

Colors
f9d9e8
85cae6
cee9f5
fee18a
ffffff
eea4c8

Requirements
Must have
• Colours matching my overall website at sarahlindqvist.com.au - pinks, light blue, gold, white
• Imagery similiar to my Instagram, see below https://www.instagram.com/riverstonecarexy/
• - soft, warm, welcoming, nurturing, safe, inviting - see image on sales page for inspiration
• contact details
Should not have
• harsh dark colours or harsh lines

```html
<!DOCTYPE html>
<html lang="en">
<head>
<meta charset="utf-8">
<title>The Quiet Bloom Gathering – Flyer</title>
<link href="https://fonts.googleapis.com/css2?family=Bree+Serif&family=Dancing+Script:wght@700&family=Montserrat:wght@400;500;600&family=Oswald:wght@500&display=swap" rel="stylesheet">
<style>
  :root{
    --bg:#f3eee9;
    --paper:#ffffff;
    --pink-deep:#c8336f;
    --pink:#e0628e;
    --pink-soft:#eea4c8;
    --blush:#f9d9e8;
    --blue:#85cae6;
    --blue-soft:#cee9f5;
    --teal:#6fc0cf;
    --gold:#fee18a;
    --ink:#5a5560;
    --sand:#efe6d6;
  }
  *{box-sizing:border-box;margin:0;padding:0}
  html,body{width:1200px;height:984px;overflow:hidden;background:var(--bg)}
  .flyer{
    position:absolute;left:260px;top:22px;width:680px;height:940px;
    background:var(--paper);box-shadow:0 6px 24px rgba(90,70,60,.15);
    overflow:hidden;font-family:"Montserrat",sans-serif;color:var(--ink);
  }
  .flyer-frame{position:absolute;inset:12px;border:1px solid #f2ecef;pointer-events:none}
  .hero{
    position:absolute;left:0;top:0;width:680px;height:420px;
    background:
      linear-gradient(90deg,rgba(255,255,255,.9) 0%,rgba(255,255,255,.45) 38%,rgba(255,255,255,0) 60%),
      linear-gradient(180deg,#d9d6e6 0%,#ecd2dc 30%,#f6cbb4 52%,#e9b6a8 58%,#9fb2c4 66%,#b8c6d2 82%,#e8e8ef 100%);
  }
  .brand{position:absolute;left:36px;top:40px;display:flex;align-items:center;gap:8px}
  .brand-dot{width:12px;height:12px;border-radius:50%;background:var(--pink-soft)}
  .brand-name{font-size:19px;font-weight:500;color:var(--blue);letter-spacing:.5px}
  .host{position:absolute;left:56px;top:78px;font-size:11px;font-weight:600;color:var(--blue);letter-spacing:1.2px}
  .title{position:absolute;left:48px;top:122px;font-family:"Bree Serif",serif;font-size:42px;line-height:1.08;font-weight:400}
  .title-line-1{color:var(--pink)}
  .title-line-2{color:var(--teal);padding-left:28px}
  .tiles{
    position:absolute;left:14px;top:318px;width:652px;
    display:grid;grid-template-columns:repeat(5,1fr);grid-template-rows:128px 128px;gap:4px;
  }
  .tile{
    display:flex;align-items:center;justify-content:center;text-align:center;padding:10px;
    font-family:"Oswald",sans-serif;font-size:12.5px;line-height:1.3;color:#fff;
  }
  .t1{background:#c8336f}.t2{background:#d9557f}.t3{background:#eb9a7c}.t4{background:#d4d79c}.t5{background:#7fc8cf}
  .t6{background:#cb3d75}.t7{background:#dc5f88}.t8{background:#ee9e7c}.t9{background:#b9dab0}.t10{background:#6fc0cf}
  .columns{position:absolute;left:30px;top:596px;width:620px;display:grid;grid-template-columns:1fr 1fr;gap:22px;font-size:9.6px;line-height:1.45}
  .points{list-style:none}
  .points>li{position:relative;padding-left:14px;margin-bottom:8px}
  .points>li::before{content:"";position:absolute;left:0;top:4px;width:6px;height:6px;background:var(--blue)}
  .points>li.pink::before{background:var(--pink-deep)}
  .lead-pink{color:var(--pink-deep)}
  .lead-blue{color:var(--blue)}
  .gifts{list-style:none;margin-top:3px}
  .gifts li{position:relative;padding-left:12px}
  .gifts li::before{content:"\2665";position:absolute;left:0;top:0;color:var(--pink-soft);font-size:9px}
  .price{color:var(--blue)}
  .socials{position:absolute;right:34px;top:812px;display:flex;gap:7px}
  .socials span{width:12px;height:12px;border-radius:50%;background:var(--pink-soft)}
  .contact{
    position:absolute;right:24px;top:832px;width:345px;height:34px;background:var(--sand);
    display:flex;align-items:center;gap:14px;padding:0 14px;font-size:11.5px;font-weight:600;color:var(--ink);
  }
  .contact-item{display:flex;align-items:center;gap:6px;white-space:nowrap}
  .contact-item.email{font-size:9px;font-weight:500}
  .ready{
    position:absolute;left:40px;top:868px;font-family:"Dancing Script",cursive;font-weight:700;
    font-size:44px;line-height:1;white-space:nowrap;
    background:linear-gradient(90deg,var(--pink-deep),var(--pink) 35%,#e9c98a 65%,var(--blue) 95%);
    -webkit-background-clip:text;background-clip:text;color:transparent;
  }
</style>
</head>
<body>
<article class="flyer">
  <div class="hero" role="img" aria-label="Soft sunset beach photo of a woman stretching her arms to the sky beside the sea"></div>
  <div class="brand"><span class="brand-dot"></span><span class="brand-name">The Soft Haven Experience</span></div>
  <p class="host">with Sarah Lindqvist</p>
  <h1 class="title"><span class="title-line-1">The Quiet Bloom</span><br><span class="title-line-2">Gathering</span></h1>

  <section class="tiles">
    <div class="tile t1">It's time to make a commitment….</div>
    <div class="tile t2">It's time for YOU, to SHOW UP for YOU…..</div>
    <div class="tile t3">It's time to truly let go… and finally heal, and find the peace that you so long for…</div>
    <div class="tile t4">You deserve to feel the freedom that comes with truly loving and accepting your body.</div>
    <div class="tile t5">You deserve the freedom that comes with experiencing a deeper trusting</div>
    <div class="tile t6">Connection with your body, where you feel safe, at home.</div>
    <div class="tile t7">Can you even imagine a whole day that you didn't hate your body,</div>
    <div class="tile t8">you didn't fight with food, and you felt peaceful and at home with your body?</div>
    <div class="tile t9">Can you love the part of you, that hates your body?</div>
    <div class="tile t10">You can't heal something you hate.</div>
  </section>

  <section class="columns">
    <ul class="points">
      <li><span class="lead-pink">It's time to show up for YOU,</span> consistently, every week, and do the work, once and for all. No more games, no more half in on YOU…. You deserve better than a life contained in the mental prison of body hatred.</li>
      <li class="pink"><span class="lead-blue">Are you truly ready to make the commitment?</span> How would it feel to be able to say, "I am free to love and accept my body", and "I am free, connected and at peace to my body"?</li>
      <li><span class="lead-pink">I am inviting 10 women only into this six-week healing experience,</span> as I personally know, that when we share our stories, it opens our hearts for other people to share their stories. It gives us the sense we are not alone in our journey's.</li>
    </ul>
    <ul class="points">
      <li class="pink">The women that come on this six-week journey will receive;
        <ul class="gifts">
          <li>One 90mins one on one coaching session with me (which for the women that have attended the Friday circle previously, can be done before this healing circle begins),</li>
          <li>Private online group to continue support outside of the circle</li>
          <li>Homework outside of circle to support your healing</li>
          <li>Journal and other small gifts weekly</li>
        </ul>
      </li>
      <li class="pink">The financial investment in <span class="lead-pink">YOU</span>, is <span class="price">$XX</span> for the six weeks. For the women that have attended the Friday night Gentle Bloom Sister Circle, you will receive a discount of <span class="lead-pink">$100</span>, taking the price to <span class="price">$XX</span>.</li>
    </ul>
  </section>

  <div class="socials" aria-hidden="true"><span></span><span></span><span></span><span></span></div>
  <div class="contact">
    <span class="contact-item">
      <svg width="16" height="14" viewBox="0 0 16 14"><path d="M2 5c0-2 3-3 6-3s6 1 6 3l-2 1-1-2H5L4 6z M4 7h8l1 6H3z" fill="#6fc0cf"/><circle cx="8" cy="10" r="1.6" fill="#efe6d6"/></svg>
      0400 555 219
    </span>
    <span class="contact-item email">
      <svg width="14" height="11" viewBox="0 0 14 11"><rect x="0.5" y="0.5" width="13" height="10" rx="1" fill="#6fc0cf"/><path d="M1 1.5l6 4.5 6-4.5" fill="none" stroke="#efe6d6" stroke-width="1.2"/></svg>
      sarah@sarahlindqvist.com.au
    </span>
  </div>
  <p class="ready">Are You Ready?</p>
  <div class="flyer-frame"></div>
</article>
</body>
</html>
```